Kem7Dex Letterhead

Need a new letterhead for my law firm.
IDENTIFYING INFORMATION BELOW:
Ansel T Brightwater III
Attorney at Law
Address: 4832 Tillbury Rd, Ste 250, Dallas, TX 75204
Phone: 866-402-7183
Fax: 469-583-0271
Email: kem@kem7dex.example
Website: www.kem7dex.example

Colors
0054AA
0677BA
7BADD7
CADEEF
E8F1F8

Requirements
Must have
• Logo needs to be on the letterhead, along with identifying information which is included in the project description.

```html
<!DOCTYPE html>
<html lang="en">
<head>
<meta charset="utf-8">
<title>Kem7Dex Letterhead</title>
<link rel="stylesheet" href="https://fonts.googleapis.com/css2?family=Roboto:wght@300;400;500;900&family=Great+Vibes&display=swap">
<style>
  :root {
    --brand-blue: #0054AA;
    --ink: #1d1d1f;
    --ink-soft: #2e2e30;
    --paper: #f3f3f3;
    --backdrop: #e6e6e6;
    --rule: #8a8a8a;
  }
  * { margin: 0; padding: 0; box-sizing: border-box; }
  html, body {
    width: 1200px; height: 1200px; overflow: hidden;
    background: var(--backdrop);
    font-family: "Roboto", "Helvetica Neue", Arial, sans-serif;
  }
  .letterhead {
    position: absolute; left: 204px; top: 40px;
    width: 792px; height: 1120px;
    background: var(--paper);
    box-shadow: 0 4px 18px rgba(0,0,0,0.12);
    overflow: hidden;
    color: var(--ink-soft);
  }
  .header-band {
    position: absolute; left: 0; top: 0; width: 100%; height: 24px;
    background: var(--brand-blue);
  }
  .header-rule {
    position: absolute; left: 77px; right: 84px; top: 148px; height: 1px;
    background: var(--brand-blue);
  }
  .brand { position: absolute; left: 77px; top: 72px; text-align: center; width: 240px; }
  .brand-name {
    font-weight: 900; font-size: 40px; letter-spacing: 3px;
    color: var(--ink); line-height: 1;
  }
  .brand-tagline {
    margin-top: 6px; font-weight: 400; font-size: 14px;
    letter-spacing: 2px; color: var(--ink);
  }
  .letter {
    position: absolute; left: 85px; top: 262px; width: 623px;
    font-weight: 300; font-size: 13.2px; line-height: 18.7px;
  }
  .letter p { margin-bottom: 18.7px; }
  .letter .body-text { text-align: justify; }
  .recipient { margin-bottom: 37px !important; }
  .closing { margin-top: 46px; margin-bottom: 0 !important; }
  .signature {
    font-family: "Great Vibes", cursive; font-size: 27px;
    color: var(--ink); line-height: 1.2; margin-top: 6px;
  }
  .footer { position: absolute; left: 0; top: 1031px; width: 100%; height: 62px; }
  .footer-accent {
    position: absolute; left: 0; top: 0; width: 10px; height: 60px;
    background: var(--brand-blue);
  }
  .attorney {
    position: absolute; left: 56px; top: 0;
    font-size: 13px; line-height: 16px; color: var(--ink);
  }
  .attorney-name { color: var(--brand-blue); font-weight: 500; }
  .footer-divider {
    position: absolute; left: 225px; top: 0; width: 1px; height: 60px;
    background: var(--rule);
  }
  .contacts {
    position: absolute; left: 244px; top: 0; list-style: none;
    font-size: 13px; line-height: 16px; color: var(--ink);
  }
  .contacts li { display: flex; align-items: center; gap: 7px; }
  .contacts svg { width: 10px; height: 10px; fill: var(--brand-blue); flex: none; }
</style>
</head>
<body>
<main class="letterhead">
  <div class="header-band"></div>
  <div class="header-rule"></div>

  <div class="brand">
    <div class="brand-name">KEM7DEX</div>
    <div class="brand-tagline">RIGHT BY YOUR SIDE</div>
  </div>

  <article class="letter">
    <p class="recipient-date">01 January 2050</p>
    <p class="recipient">Company (Pvt) Ltd.<br>PO Box 3355 Mainville St<br>Sample City Country 3355</p>
    <p>Dear Harold Vance,</p>
    <p class="body-text">Lorem ipsum dolor sit amet, consectetuer adipiscing elit, sed diam nonummy nibh euismod tincidunt ut laoreet dolore magna aliquam erat volutpat. Ut wisi enim ad minim veniam, quis nostrud exerci tation ullamcorper suscipit lobortis nisl ut aliquip ex ea commodo consequat. Duis dolore te feugait nulla facilisi. Nam liber tempor cum soluta nobis eleifend option congue nihil imperdiet doming id quod mazim placerat facer possim assum. Lorem ipsum dolor sit amet, consectetuer adipiscing elit, sed diam nonummy nibh euismod tincidunt ut laoreet dolore magna aliquam erat volutpat. Ut wisi enim ad minim veniam, quis nostrud exerci tation ullamcorper suscipit lobortis nisl ut aliquip ex ea commodo consequat.</p>
    <p class="body-text">Consectetuer adipiscing elit, sed diam nonummy nibh euismod tincidunt ut laoreet dolore magna aliquam erat volutpat. Ut wisi enim ad minim veniam, quis nostrud exerci tation ullamcorper suscipit lobortis nisl ut aliquip ex ea commodo consequat. Consectetuer adipiscing elit, sed diam nonummy nibh euismod tincidunt ut laoreet dolore magna aliquam erat volutpat. Ut wisi enim ad minim veniam, quis nostrud exerci tation ullamcorper suscipit lobortis nisl ut aliquip ex ea commodo consequat.</p>
    <p class="body-text">Consectetuer adipiscing elit, sed diam nonummy nibh euismod tincidunt ut laoreet dolore magna aliquam erat volutpat. Ut wisi enim ad minim veniam, quis nostrud exerci tation ullamcorper suscipit lobortis nisl ut aliquip ex ea commodo consequat. Consectetuer adipiscing elit, sed diam nonummy nibh euismod tincidunt ut laoreet dolore magna aliquam erat volutpat. Ut wisi enim ad minim veniam, quis nostrud exerci tation ullamcorper suscipit lobortis nisl ut aliquip ex ea commodo consequat.</p>
    <p class="closing">Sincerely Yours</p>
    <div class="signature">Marcus Ellery</div>
  </article>

  <footer class="footer">
    <div class="footer-accent"></div>
    <div class="attorney">
      <div class="attorney-name">Ansel T Brightwater III</div>
      <div>Attorney at Law</div>
      <div>4832 Tillbury Rd</div>
      <div>Ste 250, Dallas, TX 75204</div>
    </div>
    <div class="footer-divider"></div>
    <ul class="contacts">
      <li><svg viewBox="0 0 10 10"><path d="M2 0.5 L3.6 2.6 L2.7 3.6 C3.3 5 5 6.7 6.4 7.3 L7.4 6.4 L9.5 8 L8.3 9.5 C4.5 9.3 0.7 5.5 0.5 1.7 Z"/></svg>866-402-7183</li>
      <li><svg viewBox="0 0 10 10"><rect x="2.5" y="0.5" width="5" height="3"/><rect x="0.5" y="3.5" width="9" height="4" rx="1"/><rect x="2.5" y="6.5" width="5" height="3"/></svg>469-583-0271</li>
      <li><svg viewBox="0 0 10 10"><path d="M0.5 2 H9.5 V8 H0.5 Z M0.5 2 L5 5.5 L9.5 2" fill="none" stroke="var(--brand-blue)" stroke-width="1.2"/></svg>kem@kem7dex.example</li>
      <li><svg viewBox="0 0 10 10"><g fill="none" stroke="var(--brand-blue)" stroke-width="1"><circle cx="5" cy="5" r="4.3"/><ellipse cx="5" cy="5" rx="1.8" ry="4.3"/><path d="M0.7 5 H9.3"/></g></svg>www.kem7dex.example</li>
    </ul>
  </footer>
</main>
</body>
</html>
```